Criação de Kit Layout de Posts para Redes Sociais (Facebook, Instagram e etc) para Advocacia e Direito
" Escritório de advocacia inovador que visa implementar atendimento digital, via plataformas digitais (Website, Redes sociais, WhatsApp), sem descartar eventual atendimento presencial. O foco é a defesa dos direitos trabalhistas e previdenciários de pessoas físicas, com atendimento personalizado, humanizado, singular. Vestimos a camisa dos nossos clientes e utilizamos todas as técnicas jurídicas e ferramentas tecnológicas para implementar a defesa de seus direitos. "

```html
<!DOCTYPE html>
<html lang="pt-BR">
<head>
<meta charset="UTF-8">
<title>Moreira Santana Advocacia — Post</title>
<link rel="stylesheet" href="https://fonts.googleapis.com/css2?family=Arimo:wght@400&display=swap">
<style>
  :root {
    --band: #0c0c0c;
    --white: #ffffff;
    --ink: #0a0a0a;
    --sun: #fff3d6;
    --peach: #f2b48a;
    --rose: #c98a9a;
    --mauve: #8a6f8e;
    --wood: #7a4f45;
    --wood-dark: #4a2f2c;
    --sky: #b9d6d8;
  }
  * { margin: 0; padding: 0; box-sizing: border-box; }
  html, body {
    width: 1200px;
    height: 1200px;
    overflow: hidden;
    background: var(--white);
  }
  .post {
    position: relative;
    width: 1200px;
    height: 1200px;
    overflow: hidden;
  }
  .backdrop {
    position: absolute;
    inset: 0;
    background:
      radial-gradient(circle at 74% 24%, var(--sun) 0%, rgba(255,230,190,0.85) 12%, rgba(242,180,138,0.35) 32%, rgba(242,180,138,0) 52%),
      linear-gradient(180deg, var(--sky) 0%, var(--peach) 22%, var(--rose) 40%, var(--mauve) 52%, var(--wood) 68%, var(--wood-dark) 100%);
  }
  .header-band {
    position: absolute;
    left: 43px;
    top: 36px;
    width: 1121px;
    height: 156px;
    background: var(--band);
    border-top-left-radius: 40px;
  }
  .header-band::after {
    content: "";
    position: absolute;
    left: 0;
    top: 100%;
    width: 620px;
    height: 101px;
    background: var(--band);
    border-bottom-right-radius: 60px;
  }
  .brand-name {
    position: absolute;
    left: 120px;
    top: 112px;
    font-family: "Arimo", sans-serif;
    font-weight: 400;
    font-size: 40px;
    line-height: 52px;
    color: var(--white);
    z-index: 2;
  }
  .brand-name .line { display: block; }
  .contact-link {
    position: absolute;
    left: 715px;
    top: 106px;
    font-family: "Arimo", sans-serif;
    font-size: 30px;
    color: var(--white);
    letter-spacing: 0.3px;
    z-index: 2;
  }
  .headline {
    position: absolute;
    left: 580px;
    top: 378px;
    width: 500px;
    text-align: center;
    font-family: "Arimo", sans-serif;
    font-weight: 400;
    font-size: 128px;
    line-height: 124px;
    color: var(--ink);
  }
</style>
</head>
<body>
  <main class="post">
    <div class="backdrop" role="img" aria-label="Fotografia de uma passarela de madeira moderna ao pôr do sol, com estrutura metálica curva e reflexo do sol"></div>
    <div class="header-band"></div>
    <div class="brand-name">
      <span class="line">MOREIRA SANTANA</span>
      <span class="line">ADVOCACIA</span>
    </div>
    <div class="contact-link">INFORMAÇÕES/CONTATOS</div>
    <h1 class="headline">TEXTO<br>AQUI</h1>
  </main>
</body>
</html>
```